Design and Renovation Company Luxury Business Card

I want to create a luxury business card for a Design and Renovation Firm . We will use our current logo. The company name is 742BUILD. We do not want anything standard. We need a very unique concept.
Please see uploaded inspiration. I really like the textured paper option. I would like the card to be thick with debossing, and/or embossing options. The logo has orange in it but I would like to see the card with and without the orange. I think the orange may make the company feel less high-end. The goal is to elevate the logo not match its vibe per se of the logo. We want something very unique, not standard at all!
I would like a space for :
Logo,
Name,
Position,
Email,
Office number,
Website Address,
Business Address,
Thank you!
Have fun!
Target Market(s)
Home owners Age 35 +
Industry/Entity Type
Design and Renovation
Contact Information for Business Card
Logo, Name, Position, Email, Office number, Website Address, Business Address,.
Colors
Designer to choose colors to be used in the design.
Requirements
Must have
- A luxury designer feel. Must be black or dark grey but open to other luxury ideas.
Nice to have
- Gold, silver, black embossing or debossing. Textured paper design.
Should not have
- A cheap look and feel.

```html
<!DOCTYPE html>
<html lang="en">
<head>
<meta charset="utf-8">
<title>742BUILD Business Card</title>
<link rel="stylesheet" href="https://fonts.googleapis.com/css2?family=Quicksand:wght@400;700&display=swap">
<style>
  :root {
    --page: #ffffff;
    --card-light: #1d1f21;
    --card-dark: #08090a;
    --gold: #eab51a;
    --gold-deep: #d19f10;
    --rule: #5a4a14;
  }
  html, body {
    margin: 0;
    padding: 0;
    width: 1200px;
    height: 586px;
    overflow: hidden;
    background: var(--page);
  }
  .canvas {
    position: relative;
    width: 1200px;
    height: 586px;
    font-family: "Quicksand", sans-serif;
    color: var(--gold);
  }
  .card {
    position: absolute;
    top: 120px;
    width: 532px;
    height: 345px;
    background:
      radial-gradient(ellipse at 45% 40%, var(--card-light) 0%, #121314 55%, var(--card-dark) 100%);
  }
  .card--front { left: 48px; }
  .card--back { left: 620px; }

  .brand {
    position: absolute;
    display: flex;
    flex-direction: column;
    align-items: center;
  }
  .brand__square {
    background: linear-gradient(135deg, var(--gold) 0%, var(--gold-deep) 100%);
  }
  .brand__name {
    font-weight: 700;
    letter-spacing: 0.12em;
    line-height: 1;
    white-space: nowrap;
  }
  .card--front .brand {
    left: 204px;
    top: 96px;
    width: 128px;
  }
  .card--front .brand__square { width: 100px; height: 100px; margin-bottom: 26px; }
  .card--front .brand__name { font-size: 24px; }

  .card--back .brand {
    left: 110px;
    top: 110px;
    width: 104px;
  }
  .card--back .brand__square { width: 78px; height: 78px; margin-bottom: 22px; }
  .card--back .brand__name { font-size: 18px; }

  .contact {
    position: absolute;
    left: 287px;
    top: 110px;
    height: 126px;
    padding-left: 10px;
    border-left: 1px solid var(--rule);
    margin: 0;
    list-style: none;
  }
  .contact__item {
    font-size: 16px;
    line-height: 28px;
    white-space: nowrap;
  }
  .address {
    position: absolute;
    left: 0;
    right: 0;
    top: 308px;
    margin: 0;
    text-align: center;
    font-size: 16px;
    white-space: nowrap;
  }
</style>
</head>
<body>
<main class="canvas">
  <section class="card card--front" aria-label="Card front">
    <div class="brand">
      <div class="brand__square"></div>
      <div class="brand__name">742BUILD</div>
    </div>
  </section>

  <section class="card card--back" aria-label="Card back">
    <div class="brand">
      <div class="brand__square"></div>
      <div class="brand__name">742BUILD</div>
    </div>
    <ul class="contact">
      <li class="contact__item">Name</li>
      <li class="contact__item">Position</li>
      <li class="contact__item">info@742build.com</li>
      <li class="contact__item">+905 555 0147</li>
      <li class="contact__item">www.742build.ca</li>
    </ul>
    <p class="address">18 Cedar Ridge Lane Oakville, Ontario Canada L6H 0A1</p>
  </section>
</main>
</body>
</html>
```